professional business card

Professional business card with logo on one side, and underneath logo list:
- power
-data
-fibre optic
-isolar

On other side:
Marcus Trent
Owner
MOB 0492 738 204
marcus@vorpa.com.au
www.vorpaelectrical.com.au

Please edit logo to just leave VORPA

```html
<!DOCTYPE html>
<html lang="en">
<head>
<meta charset="utf-8">
<title>VORPA – Business Card</title>
<link rel="stylesheet" href="https://fonts.googleapis.com/css2?family=Open+Sans:wght@400;600;700&display=swap">
<style>
  :root {
    --teal: #1a9ea0;
    --ink: #2b2b2b;
    --muted: #6a6e70;
    --card: #ffffff;
    --backdrop: #5e5e5e;
  }
  * { margin: 0; padding: 0; box-sizing: border-box; }
  html, body {
    width: 1200px;
    height: 1200px;
    overflow: hidden;
    background: var(--backdrop);
    font-family: "Open Sans", Arial, sans-serif;
  }
  .business-card {
    position: absolute;
    left: 182px;
    top: 356px;
    width: 834px;
    height: 486px;
    background: var(--card);
    border-radius: 36px;
    overflow: hidden;
  }
  .brand {
    position: absolute;
    left: 44px;
    top: 72px;
  }
  .brand-lockup {
    display: flex;
    align-items: center;
    gap: 12px;
  }
  .brand-mark {
    width: 22px;
    height: 22px;
    background: var(--teal);
  }
  .brand-name {
    font-size: 46px;
    line-height: 1.1;
    font-weight: 700;
    color: var(--ink);
  }
  .brand-services {
    display: flex;
    gap: 7px;
    margin-top: 16px;
    list-style: none;
    font-size: 15px;
    color: var(--muted);
  }
  .brand-services li::before {
    content: "•";
    color: var(--teal);
    margin-right: 3px;
  }
  .person {
    position: absolute;
    right: 38px;
    top: 254px;
    text-align: right;
  }
  .person-name {
    font-size: 24px;
    font-weight: 700;
    color: var(--teal);
    line-height: 1.3;
  }
  .person-role {
    font-size: 22px;
    color: var(--ink);
    line-height: 1.3;
    margin-top: 2px;
  }
  .divider {
    position: absolute;
    left: 44px;
    top: 305px;
    width: 666px;
    height: 2px;
    background: var(--teal);
  }
  .side-tab {
    position: absolute;
    right: 0;
    top: 258px;
    width: 16px;
    height: 55px;
    background: var(--teal);
    border-radius: 7px 0 0 7px;
  }
  .contacts {
    position: absolute;
    left: 44px;
    top: 340px;
    list-style: none;
  }
  .contact {
    display: flex;
    align-items: center;
    gap: 9px;
    height: 35px;
    font-size: 20px;
    color: var(--muted);
  }
  .contact svg { width: 13px; height: 13px; fill: var(--teal); flex: none; }
  .bottom-band {
    position: absolute;
    left: 0;
    bottom: 0;
    width: 100%;
    height: 16px;
    background: var(--teal);
  }
</style>
</head>
<body>
  <div class="business-card">
    <div class="brand">
      <div class="brand-lockup">
        <div class="brand-mark"></div>
        <div class="brand-name">VORPA</div>
      </div>
      <ul class="brand-services">
        <li>Power</li>
        <li>Data</li>
        <li>Fibre optic</li>
        <li>Isolar</li>
      </ul>
    </div>

    <div class="person">
      <div class="person-name">Marcus Trent</div>
      <div class="person-role">Owner</div>
    </div>
    <div class="divider"></div>
    <div class="side-tab"></div>

    <ul class="contacts">
      <li class="contact">
        <svg viewBox="0 0 24 24" aria-hidden="true"><path d="M6.6 10.8a15.1 15.1 0 0 0 6.6 6.6l2.2-2.2c.3-.3.7-.4 1-.2 1.1.4 2.3.6 3.6.6.6 0 1 .4 1 1V20c0 .6-.4 1-1 1A17 17 0 0 1 3 4c0-.6.4-1 1-1h3.5c.6 0 1 .4 1 1 0 1.3.2 2.5.6 3.6.1.3 0 .7-.2 1z"/></svg>
        <span>0492 738 204</span>
      </li>
      <li class="contact">
        <svg viewBox="0 0 24 24" aria-hidden="true"><path d="M2 5h20v14H2zm2 2v.5l8 6 8-6V7l-8 6z"/></svg>
        <span>marcus@vorpa.com.au</span>
      </li>
      <li class="contact">
        <svg viewBox="0 0 24 24" aria-hidden="true"><path d="M12 2a10 10 0 1 0 0 20 10 10 0 0 0 0-20zm-1 17.9A8 8 0 0 1 4.2 10L9 14.8v1a2 2 0 0 0 2 2zm6.9-2.5A2 2 0 0 0 16 16h-1v-3a1 1 0 0 0-1-1H8v-2h2a1 1 0 0 0 1-1V7h2a2 2 0 0 0 2-2v-.4a8 8 0 0 1 2.9 12.8z"/></svg>
        <span>www.vorpaelectrical.com.au</span>
      </li>
    </ul>

    <div class="bottom-band"></div>
  </div>
</body>
</html>
```